Business Card Design for a Handbags business

We are modernising our handbags website (see attached file for new front page) and are in need of a modern business card and a related design we can use on a small marquee at the markets, on letterhead, emails etc.

As the leather handbags we mostly import are from Italy, we want a smart modern European feel to the design. We are currently thinking about changing the name of the business from Meadowlark Handbags (see www.meadowlarkhandbags.com.au) to Vantera Handbags. Also open to other suggestions you may have that communicates the European influence and quality.

Target Market(s)

25-65 year old women (and some men)

Industry/Entity Type

Business

Contact Information for Business Card

Single or double sided - whichever creates more of an impact

Font styles to use
Serif
Sans Serif

Requirements
Must have
• Clean crisp look, slightly Italian or European look and feel to reflect where the handbags are imported from
Nice to have
• open to ideas

```html
<!DOCTYPE html>
<html lang="en">
<head>
<meta charset="utf-8">
<title>Vantera Handbags – Business Card</title>
<link rel="stylesheet" href="https://fonts.googleapis.com/css2?family=Open+Sans:wght@400;600;700&display=swap">
<style>
  :root {
    --ink: #000000;
    --paper: #ffffff;
    --backdrop: #e9e7e4;
    --text-light: #ffffff;
  }
  * { margin: 0; padding: 0; box-sizing: border-box; }
  html, body {
    width: 1200px; height: 900px; overflow: hidden;
    background: var(--backdrop);
    font-family: "Open Sans", Arial, sans-serif;
  }
  .canvas { position: relative; width: 1200px; height: 900px; }

  .card { position: absolute; overflow: hidden; background: var(--ink); }

  /* Front card */
  .card--front { left: 77px; top: 34px; width: 589px; height: 364px; }
  .card--front .brand-band {
    position: absolute; left: 0; top: 0; width: 100%; height: 156px;
    background: var(--paper);
  }
  .card--front .brand { position: absolute; left: 31px; top: 36px; }

  .brand { color: var(--ink); }
  .brand__row { display: flex; align-items: center; gap: 12px; }
  .brand__mark { width: 22px; height: 22px; background: var(--ink); }
  .brand__name {
    font-weight: 600; letter-spacing: 1px; line-height: 1;
  }
  .brand__tagline {
    font-weight: 700; text-transform: uppercase; letter-spacing: 0.6px;
    line-height: 1;
  }
  .card--front .brand__name { font-size: 50px; }
  .card--front .brand__tagline { font-size: 15px; margin-top: 12px; }

  .contact { position: absolute; left: 33px; top: 186px; color: var(--text-light); }
  .contact__name { font-size: 21px; font-weight: 600; line-height: 1; }
  .contact__phone { font-size: 15px; margin-top: 14px; line-height: 1; }
  .contact__place { font-size: 15px; margin-top: 27px; line-height: 1; }
  .contact__web {
    display: flex; align-items: center; gap: 7px;
    font-size: 15px; margin-top: 31px; line-height: 1;
  }
  .contact__web svg { width: 13px; height: 13px; }

  /* Back card */
  .card--back { left: 388px; top: 505px; width: 566px; height: 352px; }
  .card--back .brand-band {
    position: absolute; left: 0; top: 98px; width: 100%; height: 155px;
    background: var(--paper);
    display: flex; align-items: center; justify-content: center;
  }
  .card--back .brand__name { font-size: 62px; }
  .card--back .brand__mark { width: 26px; height: 26px; }
  .card--back .brand__tagline { font-size: 18px; margin-top: 14px; text-align: center; }
</style>
</head>
<body>
<main class="canvas">

  <section class="card card--front" aria-label="Business card front">
    <div class="brand-band">
      <div class="brand">
        <div class="brand__row">
          <span class="brand__mark"></span>
          <span class="brand__name">Vantera</span>
        </div>
        <div class="brand__tagline">Handbags &amp; Accessories</div>
      </div>
    </div>
    <div class="contact">
      <p class="contact__name">Clara Whitfield</p>
      <p class="contact__phone">0412 555 019</p>
      <p class="contact__place">Riverbend, Brisbane</p>
      <p class="contact__web">
        <svg viewBox="0 0 14 14" aria-hidden="true">
          <circle cx="7" cy="7" r="6.3" fill="none" stroke="#fff" stroke-width="1.3"/>
          <ellipse cx="7" cy="7" rx="2.6" ry="6.3" fill="none" stroke="#fff" stroke-width="1.1"/>
          <line x1="0.7" y1="7" x2="13.3" y2="7" stroke="#fff" stroke-width="1.1"/>
        </svg>
        www.meadowlarkhandbags.com.au
      </p>
    </div>
  </section>

  <section class="card card--back" aria-label="Business card back">
    <div class="brand-band">
      <div class="brand">
        <div class="brand__row">
          <span class="brand__mark"></span>
          <span class="brand__name">Vantera</span>
        </div>
        <div class="brand__tagline">Handbags &amp; Accessories</div>
      </div>
    </div>
  </section>

</main>
</body>
</html>
```